Speisekarten
Zielgruppe
we run a restaurant and our target groups are families and business people
Aufgabenstellung
The menu consists of a black folder with 8 DIN A4 slots which have a 2 cm border on all sides. The card should be discreet, classy and easy to read without any kind of complicated fonts or pictures. we would like to see creative designs regarding our recommendation at the end of page 3.

```html
<!DOCTYPE html>
<html lang="de">
<head>
<meta charset="utf-8">
<title>Khaneh – Beilagen / Extras</title>
<link href="https://fonts.googleapis.com/css2?family=Tinos:ital@0;1&family=Source+Sans+3:wght@300;400&display=swap" rel="stylesheet">
<style>
  :root {
    --backdrop: #6e5a36;
    --paper: #ffffff;
    --brand: #6b5630;
    --title: #8c7a5c;
    --dot: #cfc4b6;
    --rule: #e6e2dc;
    --desc: #8a8886;
  }
  * { box-sizing: border-box; margin: 0; padding: 0; }
  html, body {
    width: 1200px; height: 1200px; overflow: hidden;
    background: var(--backdrop);
  }
  .menu-page {
    position: absolute; left: 220px; top: 26px;
    width: 760px; height: 1148px;
    background: var(--paper);
  }
  .masthead {
    position: absolute; left: 45px; right: 45px; top: 0; height: 92px;
  }
  .masthead .rule {
    position: absolute; top: 90px; height: 1px; background: var(--rule);
  }
  .masthead .rule-left { left: 0; width: 246px; }
  .masthead .rule-right { right: 0; width: 246px; }
  .brand-name {
    position: absolute; left: 0; right: 0; top: 50px;
    text-align: center;
    font-family: "Tinos", serif;
    font-size: 30px; letter-spacing: 2px;
    color: var(--brand);
    line-height: 32px;
  }
  .brand-underline {
    position: absolute; left: 50%; top: 90px; width: 130px; margin-left: -65px;
    height: 1px; background: var(--brand);
  }
  .section-title {
    position: absolute; left: 0; right: 0; top: 137px;
    display: flex; justify-content: center; align-items: center; gap: 28px;
    font-family: "Tinos", serif; font-style: italic;
    font-size: 29px; letter-spacing: 1px; color: var(--title);
    line-height: 36px;
  }
  .section-title .dot {
    width: 7px; height: 7px; border-radius: 50%; background: var(--dot);
  }
  .item-list {
    position: absolute; left: 45px; right: 50px; top: 196px;
    list-style: none;
  }
  .item {
    display: grid; grid-template-columns: 1fr auto;
    margin-bottom: 24px;
  }
  .item-name, .item-price {
    font-family: "Tinos", serif; font-size: 19.5px;
    line-height: 22px; color: var(--brand);
  }
  .item-price { text-align: right; }
  .item-desc {
    grid-column: 1 / 2; margin-top: 2px; max-width: 390px;
    font-family: "Source Sans 3", sans-serif; font-weight: 300;
    font-size: 15px; line-height: 19px; letter-spacing: 0.3px;
    color: var(--desc);
  }
</style>
</head>
<body>
  <main class="menu-page">
    <header class="masthead">
      <span class="rule rule-left"></span>
      <span class="brand-name">KHANEH</span>
      <span class="brand-underline"></span>
      <span class="rule rule-right"></span>
    </header>

    <h1 class="section-title"><span class="dot"></span>BEILAGEN / EXTRAS<span class="dot"></span></h1>

    <ul class="item-list">
      <li class="item"><span class="item-name">MASTO MUSIR</span><span class="item-price">4,00 €</span><p class="item-desc">Joghurt mit wilder Knoblauch</p></li>
      <li class="item"><span class="item-name">MASTO KHIAR</span><span class="item-price">4,00 €</span><p class="item-desc">Joghurt mit Gurken und Minze</p></li>
      <li class="item"><span class="item-name">KHIAR SHOUR</span><span class="item-price">3,00 €</span><p class="item-desc">Salzgurken nach persischer Art</p></li>
      <li class="item"><span class="item-name">TORSHI</span><span class="item-price">4,00 €</span><p class="item-desc">Sauer eingelegtes Gemüse</p></li>
      <li class="item"><span class="item-name">SIR TORSHI</span><span class="item-price">4,00 €</span><p class="item-desc">Eingelegter Knoblauch</p></li>
      <li class="item"><span class="item-name">BASMATIREIS</span><span class="item-price">4,00 €</span></li>
      <li class="item"><span class="item-name">BAGHALI POLO</span><span class="item-price">5,50 €</span><p class="item-desc">Basmatireis mit Bohnen, Dillspitzen und Zimt</p></li>
      <li class="item"><span class="item-name">SERESHK POLO</span><span class="item-price">5,50 €</span><p class="item-desc">Basmatireis mit gebratenen Berberitzen</p></li>
      <li class="item"><span class="item-name">SHIRIN POLO</span><span class="item-price">6,00 €</span><p class="item-desc">Basmatireis mit Mandelblättchen, gehackten Pistazien, Orangenschale und Karotten</p></li>
      <li class="item"><span class="item-name">GRILLTOMATE</span><span class="item-price">1,00 €</span><p class="item-desc">Gegrillte Tomaten</p></li>
    </ul>
  </main>
</body>
</html>
```